Quorvant Group Invitation

I need an invitation designed for both online and hard copy distribution. I'm uploading a poorly designed online invitation that includes our logo and the blue and black colors we want to use. The online invitation must have an area to embed video (see attached).

With regard to the hard copy invitation, we need it to be a 5x7 card. Where the embedded video is on the online version, we would like you to create an image that represents the terms "monetizing innovation". If you go to www.qvgroup.co, you can see what the company is using to express those words right now. There are no limitations to what you come up with for this visual.

Please note: The invitation both online and hardcopy must be designed so that all the information in the attached copy can be read. This includes: Logo, hosted by; When/date, where, two quotes, etc.

I've attached our logo files. You can use whichever logo file you want for your design.

Many thanks...looking forward to seeing all your great designs.
Updates

All - you do not need to follow our format for the invite as long as all the information we need is on it....Note:  we will need to be able to edit the information for other presentation.

EPS files of the logo have been added for those of you who have requested it.

Many thanks,

Marla

Reason: All, Apologies for the extension. The decision-makers have been travelling and have not had a chance to thoroughly review the designs. We really appreciate your patience. Many thanks, Marla

Target Market(s)

Investors and Media

Industry/Entity Type

It Company

Requirements
Must have
• Please use the blue and black colors as seen in the attached uploaded files.

```html
<!DOCTYPE html>
<html lang="en">
<head>
<meta charset="utf-8">
<title>Quorvant Group – A Special Presentation</title>
<link href="https://fonts.googleapis.com/css2?family=Open+Sans:ital,wght@0,400;0,600;0,700;0,800;1,400;1,600;1,700&display=swap" rel="stylesheet">
<style>
  :root {
    --blue: #1b5ca8;
    --blue-deep: #0c3f82;
    --blue-soft: #dbe8f5;
    --ink: #1a1a1a;
    --frame: #8e9093;
    --paper: #ffffff;
    --alert: #d0302b;
  }
  html, body {
    margin: 0;
    padding: 0;
    width: 1200px;
    height: 932px;
    overflow: hidden;
    background: var(--paper);
  }
  .invitation {
    position: relative;
    width: 1200px;
    height: 932px;
    font-family: "Open Sans", Arial, sans-serif;
    color: var(--ink);
    overflow: hidden;
    background: var(--paper);
  }
  .frame-bar {
    position: absolute;
    top: 0;
    width: 40px;
    height: 932px;
    background: linear-gradient(90deg, #a9abae, var(--frame) 60%, #7c7e81);
  }
  .frame-bar--left { left: 36px; }
  .frame-bar--right { left: 1124px; }
  .card {
    position: absolute;
    left: 76px;
    top: 0;
    width: 1048px;
    height: 932px;
    background: linear-gradient(200deg, var(--blue-soft) 0%, #ffffff 45%);
    overflow: hidden;
  }
  .card svg.waves {
    position: absolute;
    left: 0;
    top: 0;
  }
  .card p { margin: 0; }
  .headline {
    position: absolute;
    left: 0;
    width: 1048px;
    top: 58px;
    margin: 0;
    text-align: center;
    font-weight: 800;
    font-size: 47px;
    line-height: 60px;
    color: var(--blue-deep);
  }
  .brand {
    position: absolute;
    left: 300px;
    top: 150px;
    display: flex;
    align-items: center;
    gap: 96px;
  }
  .brand__mark {
    width: 108px;
    height: 140px;
    background: var(--blue);
  }
  .brand__name {
    font-weight: 700;
    font-size: 30px;
    letter-spacing: 8px;
    line-height: 42px;
    color: var(--ink);
    text-transform: uppercase;
  }
  .label {
    font-weight: 700;
    font-size: 21px;
    line-height: 29px;
    color: var(--blue-deep);
  }
  .info {
    font-size: 21px;
    line-height: 29px;
  }
  .hosts { position: absolute; left: 10px; top: 240px; }
  .when { position: absolute; left: 10px; top: 420px; }
  .where {
    position: absolute;
    left: 306px;
    top: 420px;
    padding-left: 16px;
    border-left: 3px solid var(--ink);
  }
  .video-slot {
    position: absolute;
    left: 640px;
    top: 266px;
    width: 390px;
    height: 306px;
    background: var(--paper);
    box-shadow: 0 2px 8px rgba(0,0,0,0.15);
    display: flex;
    justify-content: center;
    padding-top: 144px;
    box-sizing: border-box;
    font-weight: 700;
    font-size: 30px;
    line-height: 34px;
    color: var(--blue-deep);
  }
  .tagline {
    position: absolute;
    left: 664px;
    top: 578px;
    font-style: italic;
    font-weight: 700;
    font-size: 27px;
    line-height: 34px;
    color: var(--blue-deep);
  }
  .quote {
    position: absolute;
    left: 10px;
    font-style: italic;
    font-size: 18px;
    line-height: 27px;
    color: var(--blue-deep);
  }
  .quote--first { top: 560px; width: 440px; }
  .quote--second { top: 692px; }
  .press-name {
    position: absolute;
    font-weight: 700;
    font-size: 22px;
    line-height: 30px;
    color: var(--ink);
  }
  .press-name--first { left: 172px; top: 634px; }
  .press-name--second { left: 160px; top: 726px; }
  .rsvp {
    position: absolute;
    left: 556px;
    top: 656px;
    font-size: 20px;
    line-height: 29px;
  }
  .rsvp a, .site {
    color: var(--blue-deep);
    font-weight: 700;
    text-decoration: none;
  }
  .site {
    position: absolute;
    left: 284px;
    top: 780px;
    font-size: 28px;
    line-height: 36px;
  }
  .note {
    position: absolute;
    left: 760px;
    top: 812px;
    width: 280px;
    font-size: 16px;
    line-height: 23px;
    color: var(--paper);
  }
  .note__mark { color: var(--alert); }
</style>
</head>
<body>
<main class="invitation">
  <div class="frame-bar frame-bar--left"></div>
  <div class="frame-bar frame-bar--right"></div>

  <section class="card">
    <svg class="waves" width="1048" height="932" viewBox="0 0 1048 932" aria-hidden="true">
      <defs>
        <linearGradient id="bandBlue" x1="0" y1="0" x2="1" y2="1">
          <stop offset="0" stop-color="#2a6cb8"/>
          <stop offset="1" stop-color="#0c3f82"/>
        </linearGradient>
        <linearGradient id="topBlue" x1="0" y1="0" x2="1" y2="0">
          <stop offset="0" stop-color="#0c3f82"/>
          <stop offset="1" stop-color="#2a6cb8"/>
        </linearGradient>
        <linearGradient id="streak" x1="0" y1="0" x2="1" y2="0">
          <stop offset="0" stop-color="#9dbde2" stop-opacity="0.9"/>
          <stop offset="1" stop-color="#dbe8f5" stop-opacity="0"/>
        </linearGradient>
      </defs>
      <path d="M0 0 L344 0 Q150 40 0 190 Z" fill="url(#topBlue)"/>
      <rect x="826" y="80" width="180" height="24" fill="url(#streak)"/>
      <path d="M0 800 C300 870 700 860 1048 640 L1048 932 L0 932 Z" fill="#ffffff"/>
      <path d="M0 830 C320 890 720 870 1048 670 L1048 932 L0 932 Z" fill="url(#bandBlue)"/>
    </svg>

    <h1 class="headline">A special presentation of</h1>

    <div class="brand">
      <div class="brand__mark"></div>
      <div class="brand__name">Quorvant<br>Group</div>
    </div>

    <div class="hosts">
      <p class="label">Hosted By:</p>
      <p class="info">Reza Kalandri, CEO<br>Owen Pritchard, President<br>Luis Marquez, CFO<br>Grant Ellison, COO<br>Miles Faraday, CCO</p>
    </div>

    <div class="when">
      <p class="label">When:</p>
      <p class="info">Wednesday, September 28th<br>Check-In 3:00 pm<br>Presentation 3:30 - 4:30 pm</p>
    </div>

    <div class="where">
      <p class="label">Where:</p>
      <p class="info">Bayline Inn – Cypress Room<br>2210 Bayline Inn Ave<br>Lakemont CA 92580</p>
    </div>

    <div class="video-slot">Video</div>
    <p class="tagline">Monetizing Innovation</p>

    <p class="quote quote--first">In the biggest breakthrough against malaria in years, scientist yesterday said they had identified the odor molecules that baffle blood-thirsty mosquitoes</p>
    <p class="press-name press-name--first">The Southern Ledger</p>

    <p class="quote quote--second">Confusing mosquitoes to fight deadly disease</p>
    <p class="press-name press-name--second">Pacific Daily Courier</p>

    <p class="rsvp">Please RSVP by Monday, September 26th<br>Dana Whitfield<br>(555) 310-4826 x1003<br><a href="mailto:dwhitfield@qvgroup.co">dwhitfield@qvgroup.co</a></p>

    <a class="site" href="https://www.qvgroup.co">www.qvgroup.co</a>

    <p class="note"><span class="note__mark">*</span>Please note that you must be an accredited investor to attend the presentation.</p>
  </section>
</main>
</body>
</html>
```